Book Cover - Goals

Create book cover for book
Title: Summit Drive
Subtitle: Push Past Your Limits, Find Strength Within Yourself

See the uploaded 1st version -- I want to see different concepts -- definitely want use white space and keep a blue color similiar if not the same as the one seen in that other version and see my notes/feedback.

:

Target Market(s)

Women + Men - 35-60
Self Help + Health

Industry/Entity Type

Health And Wellness

Font styles to use
Sans Serif

Colors
0692cd
34a7d7
85cae6
cee9f5

Requirements
Must have
• Picture of father and I that can be found here:(https://files.cloudvault-share.net/folders/7K9QxRm2_41PlVnwTbZuLeHsCq3)
• and I uploaded one too (I'd like to see it with our shirts on and off)
Nice to have
• Want it to be clean
• More gender neutral -- not overly masculine or femine
• I really like these book covers - so something similair woudl be great"
• Steady Steps: The 9-Week Meal Rhythm Method
• The Quiet Harvest Plan : Retune Your Habits for Gentle Fat Burning, Steady Vigor and Lasting Stamina
• Walk Far, Feel Light for Years

```html
<!DOCTYPE html>
<html lang="en">
<head>
<meta charset="utf-8">
<title>The Summit Drive – Book Cover</title>
<link href="https://fonts.googleapis.com/css2?family=Russo+One&family=Montserrat:wght@600;700&display=swap" rel="stylesheet">
<style>
  :root {
    --navy: #1f3f8c;
    --blue: #0692cd;
    --blue-mid: #34a7d7;
    --blue-soft: #85cae6;
    --blue-pale: #cee9f5;
    --paper: #f7f8f9;
    --stage: #ececec;
  }
  * { box-sizing: border-box; margin: 0; padding: 0; }
  html, body { width: 1200px; height: 927px; overflow: hidden; background: var(--stage); }
  .cover {
    position: absolute; left: 320px; top: 34px;
    width: 560px; height: 860px;
    background: var(--paper);
    overflow: hidden;
    box-shadow: 0 6px 20px rgba(0,0,0,.12);
  }
  .cover__sky { position: absolute; left: 0; top: 0; width: 560px; height: 420px; }
  .cover__authors {
    position: absolute; left: 0; right: 0; top: 34px;
    text-align: center; color: #fff;
    font-family: 'Montserrat', sans-serif; font-weight: 700;
    letter-spacing: 1px;
  }
  .cover__names { font-size: 26px; line-height: 1.1; }
  .cover__team { font-size: 15px; margin-top: 4px; font-weight: 600; }
  .cover__title {
    position: absolute; left: 34px; top: 118px;
    font-family: 'Russo One', sans-serif; color: var(--navy);
    line-height: .86;
  }
  .cover__title-the { display: block; font-size: 28px; }
  .cover__title-main { display: block; font-size: 92px; letter-spacing: 1px; }
  .cover__photo {
    position: absolute; left: 90px; top: 330px;
    width: 400px; height: 475px;
    background: linear-gradient(180deg, #e7b99a 0%, #d99a74 45%, #4a7fb8 78%, #2c5a99 100%);
    border-radius: 4px;
  }
  .cover__band {
    position: absolute; left: 0; right: 0; bottom: 0; height: 54px;
    background: var(--navy);
    display: flex; align-items: center; justify-content: center;
    font-family: 'Montserrat', sans-serif; font-weight: 700;
    font-size: 14.5px; color: #fff; text-transform: uppercase; letter-spacing: .4px;
  }
</style>
</head>
<body>
  <main class="cover">
    <svg class="cover__sky" viewBox="0 0 560 420" aria-hidden="true">
      <defs>
        <linearGradient id="skyFade" x1="0" y1="0" x2="0" y2="1">
          <stop offset="0" stop-color="var(--blue)"/>
          <stop offset=".28" stop-color="var(--blue-mid)"/>
          <stop offset=".62" stop-color="var(--blue-pale)"/>
          <stop offset="1" stop-color="var(--paper)"/>
        </linearGradient>
      </defs>
      <path d="M0,0 H560 V330 Q280,420 0,360 Z" fill="url(#skyFade)"/>
      <path d="M0,372 Q280,432 560,342" fill="none" stroke="var(--blue-soft)" stroke-width="3"/>
    </svg>
    <div class="cover__authors">
      <p class="cover__names">DALE &amp; OWEN MARSH</p>
      <p class="cover__team">THE FATHER &amp; SON FITNESS TEAM</p>
    </div>
    <h1 class="cover__title">
      <span class="cover__title-the">THE</span>
      <span class="cover__title-main">SUMMIT</span>
      <span class="cover__title-main">DRIVE</span>
    </h1>
    <div class="cover__photo" role="img" aria-label="Photo of father and son standing back to back, shirtless, arms crossed, in board shorts"></div>
    <footer class="cover__band">Push Past Your Limits, Find Strength Within Yourself</footer>
  </main>
</body>
</html>
```